Website Redesign for a Bar Association

Design a user-friendly website that promotes the most important content and drives user engagement. Directional site map (navigation & content flow) document attached.

Existing Website: http://kestrelcounsel.org/

Competitive Site Inspiration:
https://www.orvalegal.org
https://www.tqlegal.org

Must use one of the following Wordpress themes:
https://plodskins.com/lite/?theme=ravelpage_lite
https://preview.skinvoro.com/?demo=brisktopics

Industry/Entity Type

Legal

Font styles to use
Serif
Sans Serif

Colors
0355a3
f37122

Requirements
Must have
• KCA Logo

```html
<!DOCTYPE html>
<html lang="en">
<head>
<meta charset="utf-8">
<title>Kestrel Counsel Association</title>
<link href="https://fonts.googleapis.com/css2?family=Lato:wght@300;400;700;900&family=Roboto+Slab:wght@400;500;600&display=swap" rel="stylesheet">
<style>
:root{
  --navy:#2b3a5e;
  --navy-dark:#243152;
  --orange:#f4690f;
  --sky:#8fbad8;
  --text:#555;
  --panel:#f1f1f3;
}
*{margin:0;padding:0;box-sizing:border-box}
html,body{width:1200px;height:2282px;overflow:hidden}
body{position:relative;font-family:'Lato',sans-serif;color:var(--text)}
.backdrop{position:absolute;inset:0;background:linear-gradient(180deg,#3d3f6e 0%,#5a5a86 35%,#3a3f66 60%,#2d2f4e 100%)}
.page{position:absolute;left:112px;top:0;width:977px;height:2156px;background:#fff}
.abs{position:absolute}
/* header */
.brand{left:22px;top:18px;display:flex;align-items:center;gap:10px}
.brand-mark{width:58px;height:58px;border-radius:50%;background:var(--navy)}
.brand-name{font-family:'Lato',sans-serif;font-weight:900;color:var(--navy);font-size:22px;line-height:22px;letter-spacing:.3px;text-transform:uppercase}
.btn{display:flex;align-items:center;justify-content:center;gap:8px;font-weight:700;color:#fff;border-radius:3px;font-size:16px}
.btn-donate{left:673px;top:42px;width:109px;height:42px;background:var(--orange);font-weight:400;font-size:17px}
.btn-login{left:802px;top:42px;width:156px;height:42px;background:var(--navy);font-size:15px}
.nav{left:0;top:128px;width:977px;height:42px;background:var(--orange);display:flex;align-items:center}
.nav a{color:#fff;text-decoration:none;font-size:16px;padding:0 12.5px;height:42px;line-height:42px}
.nav a.active{background:var(--navy);padding:0 12px 0 24px;width:80px}
/* slider */
.hero{left:21px;top:192px;width:612px;height:345px;background:linear-gradient(135deg,#d9d6d0,#b8b3aa 50%,#8f8a82)}
.hero-caption{left:306px;top:0;width:306px;height:181px;background:rgba(43,58,94,.92);color:#fff;padding:18px 16px}
.hero-caption h1{font-family:'Roboto Slab',Georgia,serif;font-weight:500;font-size:31px;line-height:31px;margin-bottom:17px}
.hero-caption p{font-size:16px;line-height:21px}
.dots{left:286px;top:308px;display:flex;gap:3px}
.dots span{width:11px;height:11px;border-radius:50%;border:1.5px solid #fff}
.dots span.on{background:#fff}
/* section headings */
.sec-title{height:32px;border-bottom:3px solid var(--navy)}
.sec-title h2{display:inline-block;height:32px;background:var(--navy);color:#fff;font-family:'Roboto Slab',Georgia,serif;font-weight:600;font-size:17px;line-height:30px;padding:0 11px}
/* items */
.item{display:flex;gap:12px}
.thumb{flex:none;width:74px;height:56px}
.item h3{font-family:'Roboto Slab',Georgia,serif;font-weight:500;font-size:14.5px;color:var(--navy);line-height:22px;margin-top:4px}
.item a{color:var(--orange);font-size:12px;font-weight:700;text-decoration:none;line-height:18px}
.meta{font-size:12px;color:#666;display:flex;gap:20px;align-items:center}
.meta span{display:flex;align-items:center;gap:3px}
/* about */
.about-text{left:32px;top:1391px;width:233px;font-size:13px;line-height:23.2px;text-align:justify;font-weight:300;color:#444}
.btn-more{left:32px;top:1676px;width:149px;height:38px;background:var(--orange);border-radius:19px;font-size:14px}
/* sidebar */
.search-panel{left:658px;top:236px;width:295px;height:62px;background:var(--panel)}
.search-input{position:absolute;left:30px;top:16px;width:238px;height:30px;background:#fff;border:1px solid #e2e2e2;font-size:12px;color:#888;padding:8px 12px}
.donate-img{left:658px;top:363px;width:301px;height:210px;background:linear-gradient(120deg,#c04a2e,#8c3220 45%,#dcd8cf 60%,#6b4a30)}
.btn-donate-now{left:83px;top:139px;width:135px;height:41px;background:var(--orange);font-size:15px;border-radius:3px}
.features{left:659px;top:1320px;width:295px;list-style:none}
.features li{display:flex;gap:11px;font-size:13px;line-height:18px;color:#555;margin-bottom:9.5px}
.features svg{flex:none;margin-top:2px}
/* footer */
.footer{left:0;top:1813px;width:977px;height:292px;background:var(--navy);color:#fff}
.footer .brand-name{color:#fff;font-size:19px;line-height:19px}
.footer-about{left:35px;top:128px;width:280px;font-size:13.5px;line-height:19.6px;font-weight:400}
.fcol h4{font-weight:400;font-size:18px;margin-bottom:19px}
.fcol a{display:block;color:#fff;text-decoration:none;font-size:14px;line-height:25.7px}
.bottom-bar{left:0;top:2105px;width:977px;height:51px;background:var(--sky);color:#fff;font-size:15px}
.social{position:absolute;top:11px;width:29px;height:29px;border:1.5px solid #fff;border-radius:50%}
</style>
</head>
<body>
<div class="backdrop" role="img" aria-label="Night aerial view of a city skyline"></div>

<div class="page">
  <div class="abs brand">
    <div class="brand-mark"></div>
    <div class="brand-name">Kestrel Counsel<br>Association</div>
  </div>
  <div class="abs btn btn-donate">DONATE</div>
  <div class="abs btn btn-login">
    <svg width="16" height="14" viewBox="0 0 16 14"><path d="M8 13.5 1.6 7.2A4 4 0 0 1 8 2.4a4 4 0 0 1 6.4 4.8Z" fill="#fff"/></svg>
    MEMBER LOGIN
  </div>
  <nav class="abs nav">
    <a class="active">Home</a><a>About</a><a>Member Resoures</a><a>Programs</a><a>Scholarships</a><a>Community Resources</a><a>News and Events</a><a>Contact Us</a>
  </nav>

  <div class="abs hero" role="img" aria-label="Lawyers in suits talking on courthouse steps">
    <div class="abs hero-caption">
      <h1>Achieving Equal Justice</h1>
      <p>The Kestrel Counsel Association was established by a number of African-American attorneys during the 1930’s.</p>
    </div>
    <div class="abs dots"><span></span><span></span><span class="on"></span><span></span><span></span></div>
  </div>

  <div class="abs sec-title" style="left:21px;top:586px;width:612px"><h2>Member Resources</h2></div>
  <div class="abs item" style="left:21px;top:638px"><div class="thumb" role="img" aria-label="Scales of justice on a desk" style="background:linear-gradient(135deg,#e8e6e2,#b9b3a8)"></div><div><h3>Members Only Directory 2015-16</h3><a>Password protected</a></div></div>
  <div class="abs item" style="left:340px;top:638px"><div class="thumb" role="img" aria-label="Team meeting around a table" style="background:linear-gradient(135deg,#d3d0cc,#6d7280)"></div><div><h3>Members Only Directory 2015-16</h3><a>Password protected</a></div></div>
  <div class="abs item" style="left:21px;top:729px"><div class="thumb" role="img" aria-label="Gavel and scales in warm light" style="background:linear-gradient(135deg,#e2903d,#7a3a12)"></div><div><h3>Members Only Directory 2014-15</h3><a>Password protected</a></div></div>
  <div class="abs item" style="left:340px;top:729px"><div class="thumb" role="img" aria-label="Colleagues reviewing documents" style="background:linear-gradient(135deg,#8a6a4a,#2e2a28)"></div><div><h3>Sustaining Members</h3><a>View All Members</a></div></div>
  <div class="abs item" style="left:21px;top:819px"><div class="thumb" role="img" aria-label="Handshake by an office window" style="background:linear-gradient(135deg,#dfe6ec,#8799a8)"></div><div><h3>Public Directory</h3><a>Password protected</a></div></div>
  <div class="abs item" style="left:340px;top:819px"><div class="thumb" role="img" aria-label="Two professionals at a laptop" style="background:linear-gradient(135deg,#6c5a4c,#1f1b1a)"></div><div><h3>Financial Members</h3><a>View All Members</a></div></div>

  <div class="abs sec-title" style="left:21px;top:955px;width:612px"><h2 style="padding:0 27px 0 27px">Public Resources</h2></div>
  <div class="abs item" style="left:21px;top:1007px"><div class="thumb" role="img" aria-label="Candlelit banquet hall" style="background:linear-gradient(135deg,#c4552a,#4a1a10)"></div><div><h3>Harlow County Clerk</h3><a>View More</a></div></div>
  <div class="abs item" style="left:340px;top:1007px"><div class="thumb" role="img" aria-label="Business meeting in an office" style="background:linear-gradient(135deg,#c9cbcc,#5b6470)"></div><div><h3>US District Court for the Eastern<br>District of Norvale</h3></div></div>
  <div class="abs item" style="left:21px;top:1098px"><div class="thumb" role="img" aria-label="Open law book" style="background:linear-gradient(135deg,#f3d8b0,#a0622c)"></div><div><h3>Third Judicial Circuit of Norvale</h3><a>View More</a></div></div>
  <div class="abs item" style="left:340px;top:1098px"><div class="thumb" role="img" aria-label="Joined hands" style="background:linear-gradient(135deg,#c98b60,#6a3b22)"></div><div><h3>State Bar of&nbsp; Norvale</h3><a>View More</a></div></div>
  <div class="abs item" style="left:21px;top:1188px"><div class="thumb" role="img" aria-label="Attorney writing at a desk" style="background:linear-gradient(135deg,#eeeae4,#6d5a50)"></div><div><h3>Harlow District Court</h3><a>View More</a></div></div>
  <div class="abs item" style="left:340px;top:1188px"><div class="thumb" role="img" aria-label="Gavel beside law books" style="background:linear-gradient(135deg,#a8a8a4,#2d2b28)"></div><div><h3>Mediation Panel Association</h3><a>View More</a></div></div>

  <div class="abs sec-title" style="left:21px;top:1314px;width:612px"><h2 style="padding:0 32px 0 28px">About The KCA</h2></div>
  <div class="abs" style="left:226px;top:1415px;width:75px;height:230px;background:#f0efee"></div>
  <div class="abs" role="img" aria-label="Attorneys meeting around a conference table" style="left:301px;top:1415px;width:332px;height:230px;background:linear-gradient(135deg,#b08a64,#6a4a34 50%,#c46a3a)"></div>
  <p class="abs about-text">The Kestrel Counsel Association was established by a number of African-American attorneys during the 1930’s. It was organized to coordinate the energies and talents of the increasing number of African-Americans admitted to practice throughout Norvale. From its inception, the Kestrel Counsel Association assumed a leadership role in community and political activities. The role continues to be paramount in its endeavors today.</p>
  <div class="abs btn btn-more">READ MORE
    <svg width="13" height="13" viewBox="0 0 13 13"><circle cx="6.5" cy="6.5" r="5.5" fill="none" stroke="#fff" stroke-width="1.6"/><path d="M5 4l2.5 2.5L5 9" fill="none" stroke="#fff" stroke-width="1.6"/></svg>
  </div>

  <div class="abs sec-title" style="left:658px;top:184px;width:295px"><h2>Member Search Widget</h2></div>
  <div class="abs search-panel"><div class="search-input">Search...</div></div>
  <div class="abs sec-title" style="left:658px;top:312px;width:295px"><h2 style="width:201px">Donate Now</h2></div>
  <div class="abs donate-img" role="img" aria-label="Red chairs around a boardroom table">
    <div class="abs btn btn-donate-now">DONATE NOW</div>
  </div>

  <div class="abs sec-title" style="left:658px;top:621px;width:295px"><h2 style="width:201px">Upcoming Events</h2></div>
  <div class="abs item" style="left:659px;top:673px"><div class="thumb" role="img" aria-label="Guests at a formal ball" style="background:linear-gradient(135deg,#7a3a34,#2a1c20)"></div><div><h3>59th Annual Barristers’ Ball</h3><div class="meta"><span>▦ 16 March</span><span>◌ in Event</span></div></div></div>
  <div class="abs item" style="left:659px;top:764px"><div class="thumb" role="img" aria-label="Attorneys at a holiday gathering" style="background:linear-gradient(135deg,#c9ccd2,#3d4656)"></div><div><h3>Kestrel Counsel Association<br>Holiday</h3><div class="meta"><span>▦ 19 March</span><span>◌ in Event</span></div></div></div>
  <div class="abs item" style="left:659px;top:855px"><div class="thumb" role="img" aria-label="Law students walking" style="background:linear-gradient(135deg,#d0d4d6,#4a5058)"></div><div><h3>Law Student Reception</h3><div class="meta"><span>▦ 09 October</span><span>◌ in Event</span></div></div></div>
  <div class="abs item" style="left:659px;top:947px"><div class="thumb" role="img" aria-label="Crowded student audience" style="background:linear-gradient(135deg,#8a96b4,#3a3e5a)"></div><div><h3>Students: Winter 2018 Judicial</h3><div class="meta"><span>▦ 09 October</span><span>◌ in Event</span></div></div></div>
  <div class="abs item" style="left:659px;top:1039px"><div class="thumb" role="img" aria-label="Courtroom interior" style="background:linear-gradient(135deg,#c89a6a,#6a4a30)"></div><div><h3>25th Annual Trailblazers Dinner</h3><div class="meta"><span>▦ 03 June</span><span>◌ in Event</span></div></div></div>
  <div class="abs item" style="left:659px;top:1131px"><div class="thumb" role="img" aria-label="Lecture hall seats" style="background:linear-gradient(135deg,#b46a3c,#3e2418)"></div><div><h3>59th Annual Barristers’ Ball</h3><div class="meta"><span>▦ 16 March</span><span>◌ in Event</span></div></div></div>

  <div class="abs sec-title" style="left:658px;top:1252px;width:295px"><h2 style="width:201px;padding-left:20px">Featured</h2></div>
  <ul class="abs features">
    <li><svg width="12" height="12" viewBox="0 0 12 12"><circle cx="6" cy="6" r="6" fill="#f4690f"/><path d="M3.2 6.2l2 2 3.6-3.8" fill="none" stroke="#fff" stroke-width="1.6"/></svg>To serve the needs of our members.</li>
    <li><svg width="12" height="12" viewBox="0 0 12 12"><circle cx="6" cy="6" r="6" fill="#f4690f"/><path d="M3.2 6.2l2 2 3.6-3.8" fill="none" stroke="#fff" stroke-width="1.6"/></svg>To support and improve the justice system.</li>
    <li><svg width="12" height="12" viewBox="0 0 12 12"><circle cx="6" cy="6" r="6" fill="#f4690f"/><path d="M3.2 6.2l2 2 3.6-3.8" fill="none" stroke="#fff" stroke-width="1.6"/></svg>To provide leadership on major issues affecting the profession and the community.</li>
    <li><svg width="12" height="12" viewBox="0 0 12 12"><circle cx="6" cy="6" r="6" fill="#f4690f"/><path d="M3.2 6.2l2 2 3.6-3.8" fill="none" stroke="#fff" stroke-width="1.6"/></svg>To raise and maintain the professional and ethical standards of conduct of the Bar.</li>
    <li><svg width="12" height="12" viewBox="0 0 12 12"><circle cx="6" cy="6" r="6" fill="#f4690f"/><path d="M3.2 6.2l2 2 3.6-3.8" fill="none" stroke="#fff" stroke-width="1.6"/></svg>To promote meaningful access to justice for all persons regardless of their economic or social conditions.</li>
    <li><svg width="12" height="12" viewBox="0 0 12 12"><circle cx="6" cy="6" r="6" fill="#f4690f"/><path d="M3.2 6.2l2 2 3.6-3.8" fill="none" stroke="#fff" stroke-width="1.6"/></svg>To promote diversity within the legal profession.</li>
    <li><svg width="12" height="12" viewBox="0 0 12 12"><circle cx="6" cy="6" r="6" fill="#f4690f"/><path d="M3.2 6.2l2 2 3.6-3.8" fill="none" stroke="#fff" stroke-width="1.6"/></svg>To promote responsibility for public service by the profession.</li>
    <li><svg width="12" height="12" viewBox="0 0 12 12"><circle cx="6" cy="6" r="6" fill="#f4690f"/><path d="M3.2 6.2l2 2 3.6-3.8" fill="none" stroke="#fff" stroke-width="1.6"/></svg>To build and maintain a strong financial and organizational infrastructure to carry out the goals of the Association.</li>
  </ul>

  <footer class="abs footer">
    <div class="abs brand" style="left:35px;top:36px">
      <div class="brand-mark" style="width:44px;height:44px;background:#fff"></div>
      <div class="brand-name">Kestrel Counsel<br>Association</div>
    </div>
    <p class="abs footer-about">The Kestrel Counsel Association was established by a number of African-American attorneys during the 1930’s. It was organized to coordinate the energies and talents of the increasing number of African-Americans admitted to practice throughout Norvale.</p>
    <div class="abs fcol" style="left:387px;top:86px"><h4>Company</h4><a>About</a><a>Scholarships</a><a>Community Resources</a><a>News and Events</a><a>Contact Us</a></div>
    <div class="abs fcol" style="left:597px;top:86px"><h4>Member Resources</h4><a>Member Directory</a><a>Get Involved</a><a>Jobs</a><a>Member</a><a>On the Move</a></div>
    <div class="abs fcol" style="left:803px;top:86px"><h4>Programs</h4><a>Law School Pipeline</a><a>Summer Clerkship</a><a>Judicial Externship</a><a>Pipeline Programs</a><a>Minority Bar Passage</a></div>
  </footer>
  <div class="abs bottom-bar">
    <span class="abs" style="left:35px;top:15px">© Copyright 2020 kestrelcounsel. All Rights Reserved</span>
    <span class="social" style="left:802px"></span>
    <span class="social" style="left:840px"></span>
    <span class="social" style="left:878px"></span>
    <span class="social" style="left:917px"></span>
  </div>
</div>
</body>
</html>
```